8 1/2 x 11 Flyer Design for Water Damage Restoration Company

Houston Texas based Water Damage Restoration company is needing a advertising flyer that highlights water damage and water extraction.

KESTRAL Emergency Services
52710 Harlow Crossing Suite G4
Houston, Texas 77193
713-846-5170
www.KESTRAL58129.example

Water Damage Restoration
Water Extraction
Mold Prevention
24/7/365
FREE Evaluations

Suggested photos to use:
Water Damage
Leaking Pipes
Water on floors and ground
Water pouring from ceilings
Technicians
Company Logo
Photos

Company Colors:
Orange and Blue

```html
<!DOCTYPE html>
<html lang="en">
<head>
<meta charset="utf-8">
<title>KESTRAL Emergency Services – Flyer</title>
<link rel="stylesheet" href="https://fonts.googleapis.com/css2?family=Barlow+Condensed:wght@600;700&family=Poppins:wght@500;600;700&display=swap">
<style>
  :root{
    --navy:#1f3a68;
    --navy-deep:#18305a;
    --blue:#2d5a95;
    --orange:#ff6a0d;
    --orange-dark:#e65300;
    --brown:#7a4a2a;
    --paper:#ffffff;
    --stage:#d3d3d5;
    --mist:#eceef1;
  }
  *{box-sizing:border-box;margin:0;padding:0}
  html,body{width:1200px;height:2336px;overflow:hidden;background:var(--stage)}
  .flyer{position:absolute;left:100px;top:517px;width:1000px;height:1302px;background:var(--paper);overflow:hidden;box-shadow:0 20px 40px rgba(0,0,0,.18);font-family:"Poppins",sans-serif}
  .flyer svg.shapes{position:absolute;inset:0}
  .t{position:absolute;white-space:nowrap}
  .brand{left:66px;top:78px;display:flex;align-items:center;gap:14px}
  .brand-dot{width:34px;height:34px;border-radius:50%;background:var(--orange)}
  .brand-name{font-family:"Barlow Condensed",sans-serif;font-weight:700;font-size:60px;color:var(--navy);letter-spacing:1px;line-height:1}
  .headline{left:60px;top:212px;font-family:"Barlow Condensed",sans-serif;font-weight:700;font-size:100px;line-height:86px;color:var(--navy)}
  .headline .accent{color:var(--orange)}
  .service{left:157px;color:#fff;font-weight:600;font-size:36px;line-height:44px}
  .ribbon-a{left:150px;top:975px;font-weight:700;font-size:34px;color:#fff}
  .ribbon-b{left:152px;top:1017px;font-weight:700;font-size:31px;color:#fff}
  .free{left:376px;top:930px;font-family:"Barlow Condensed",sans-serif;font-weight:700;font-size:104px;line-height:1;color:var(--orange)}
  .evaluations{left:380px;top:1026px;width:188px;height:46px;background:var(--navy);color:#fff;font-family:"Barlow Condensed",sans-serif;font-weight:600;font-size:40px;line-height:46px;text-align:center}
  .call-tab{left:62px;top:1101px;font-weight:700;font-size:24px;color:#fff;letter-spacing:.3px}
  .phone{left:103px;top:1143px;font-weight:700;font-size:38px;color:#fff}
  .address{left:103px;top:1202px;font-weight:500;font-size:18px;line-height:24px;color:#fff}
  .website{left:617px;width:389px;top:1224px;text-align:center;font-weight:700;font-size:22px;color:#fff;letter-spacing:.5px}
</style>
</head>
<body>
<main class="flyer">
  <svg class="shapes" width="1000" height="1302" viewBox="0 0 1000 1302">
    <defs>
      <linearGradient id="hero-bg" x1="0" y1="0" x2="1" y2="0">
        <stop offset="0" stop-color="#ffffff"/>
        <stop offset=".45" stop-color="#f1f2f4"/>
        <stop offset="1" stop-color="#d9dce0"/>
      </linearGradient>
      <linearGradient id="band" x1="0" y1="0" x2="1" y2="1">
        <stop offset="0" stop-color="var(--navy)"/>
        <stop offset="1" stop-color="var(--blue)"/>
      </linearGradient>
      <linearGradient id="tech" x1="0" y1="0" x2="0" y2="1">
        <stop offset="0" stop-color="#c9d0da"/>
        <stop offset=".5" stop-color="#2f55b8"/>
        <stop offset="1" stop-color="#24449a"/>
      </linearGradient>
      <linearGradient id="flood-a" x1="0" y1="0" x2="0" y2="1">
        <stop offset="0" stop-color="#e8ebee"/><stop offset="1" stop-color="#3b4a5e"/>
      </linearGradient>
      <linearGradient id="flood-b" x1="0" y1="0" x2="1" y2="1">
        <stop offset="0" stop-color="#dfe4ea"/><stop offset="1" stop-color="#8796a8"/>
      </linearGradient>
      <linearGradient id="flood-c" x1="0" y1="0" x2="0" y2="1">
        <stop offset="0" stop-color="#d8c9a4"/><stop offset="1" stop-color="#eef0f1"/>
      </linearGradient>
      <linearGradient id="flood-d" x1="0" y1="0" x2="0" y2="1">
        <stop offset="0" stop-color="#e9e3d8"/><stop offset="1" stop-color="#7d8794"/>
      </linearGradient>
    </defs>

    <rect x="0" y="0" width="1000" height="503" fill="url(#hero-bg)" role="img" aria-label="Faded photo of a service van parked in front of a warehouse"/>
    <rect x="0" y="502" width="1000" height="407" fill="url(#band)"/>

    <rect x="600" y="62" width="395" height="462" rx="40" fill="url(#tech)" opacity=".85" role="img" aria-label="Photo of a smiling technician in blue overalls sitting cross-legged beside a plunger"/>

    <!-- service dividers -->
    <line x1="62" y1="645" x2="500" y2="645" stroke="#9fb3d3" stroke-width="1.5" stroke-dasharray="5 4"/>
    <line x1="62" y1="775" x2="500" y2="775" stroke="#9fb3d3" stroke-width="1.5" stroke-dasharray="5 4"/>

    <!-- service drop icons -->
    <g class="drop-icon" transform="translate(66,528)">
      <path d="M32 0 C40 28 66 50 66 76 A34 34 0 0 1 -2 76 C-2 50 24 28 32 0Z" fill="var(--orange)" stroke="#fff" stroke-width="3"/>
      <path d="M14 84 q9 -6 18 0 t18 0 M18 70 h28 v-12 h-28z" fill="none" stroke="#fff" stroke-width="3"/>
    </g>
    <g class="drop-icon" transform="translate(66,658)">
      <path d="M32 0 C40 28 66 50 66 76 A34 34 0 0 1 -2 76 C-2 50 24 28 32 0Z" fill="var(--orange)" stroke="#fff" stroke-width="3"/>
      <path d="M32 50 c5 8 7 12 0 16 c-7 -4 -5 -8 0 -16z M14 84 h36 M18 74 h28" fill="none" stroke="#fff" stroke-width="3"/>
    </g>
    <g class="drop-icon" transform="translate(60,788)">
      <path d="M32 0 C40 28 66 50 66 76 A34 34 0 0 1 -2 76 C-2 50 24 28 32 0Z" fill="var(--orange)" stroke="#fff" stroke-width="3"/>
      <circle cx="25" cy="72" r="11" fill="none" stroke="#fff" stroke-width="3"/>
      <circle cx="42" cy="86" r="8" fill="none" stroke="#fff" stroke-width="3"/>
      <line x1="36" y1="80" x2="48" y2="92" stroke="#fff" stroke-width="3"/>
    </g>

    <!-- hexagon photo tiles -->
    <polygon points="677,671 747,550 885,550 954,671 885,792 747,792" fill="url(#flood-a)" stroke="var(--orange)" stroke-width="6" role="img" aria-label="Photo of a flooded modern kitchen"/>
    <polygon points="520,822 589,701 728,701 797,822 728,943 589,943" fill="url(#flood-b)" stroke="var(--orange)" stroke-width="6" role="img" aria-label="Photo of a plumber's gloved hands repairing a leaking pipe with a wrench"/>
    <polygon points="730,928 799,807 937,807 1006,928 937,1049 799,1049" fill="url(#flood-c)" stroke="var(--orange)" stroke-width="6" role="img" aria-label="Photo of water pouring from a damaged ceiling"/>
    <polygon points="607,1080 677,959 815,959 885,1080 815,1201 677,1201" fill="url(#flood-d)" stroke="var(--orange)" stroke-width="6" role="img" aria-label="Photo of a flooded living room with sofa and curtains"/>

    <!-- clock -->
    <g class="clock">
      <path d="M140 962 A55 55 0 1 0 166 1030" fill="none" stroke="var(--navy)" stroke-width="9" stroke-linecap="round"/>
      <polyline points="116,958 116,1002 100,1018" fill="none" stroke="var(--navy)" stroke-width="7" stroke-linecap="round" stroke-linejoin="round"/>
    </g>
    <!-- ribbons -->
    <polygon points="135,974 270,974 285,994 270,1014 135,1014" fill="var(--orange)"/>
    <polygon points="135,1014 320,1014 335,1036 320,1058 135,1058" fill="var(--navy)"/>
    <rect x="135" y="1014" width="14" height="44" fill="var(--brown)"/>
    <line x1="357" y1="940" x2="357" y2="1080" stroke="#d6d9de" stroke-width="2"/>

    <!-- contact band -->
    <polygon points="0,1122 567,1122 617,1232 577,1302 0,1302" fill="var(--navy)"/>
    <path d="M0 1097 h262 a20 20 0 0 1 20 20 v20 h-282z" fill="var(--orange)"/>
    <polygon points="617,1214 1006,1214 1006,1302 577,1302 603,1246" fill="var(--orange)"/>

    <!-- phone icon -->
    <g transform="translate(64,1152)">
      <circle cx="15" cy="15" r="14" fill="none" stroke="var(--orange)" stroke-width="4"/>
      <path d="M9 9 l4 -1 l3 5 l-2 2 c1 3 3 5 6 6 l2 -2 l5 3 l-1 4 c-9 0 -17 -8 -17 -17z" fill="var(--orange)"/>
    </g>
    <!-- pin icon -->
    <g transform="translate(68,1206)">
      <path d="M11 0 a11 11 0 0 1 11 11 c0 8 -11 18 -11 18 s-11 -10 -11 -18 a11 11 0 0 1 11 -11z" fill="var(--orange)"/>
      <circle cx="11" cy="11" r="4" fill="#fff"/>
      <ellipse cx="11" cy="31" rx="11" ry="3" fill="none" stroke="var(--orange)" stroke-width="2"/>
    </g>
  </svg>

  <div class="t brand"><span class="brand-dot"></span><span class="brand-name">KESTRAL</span></div>

  <h1 class="t headline">KESTRAL<br><span class="accent">EMERGENCY</span><br>SERVICES</h1>

  <p class="t service" style="top:535px">Water Damage<br>Restoration</p>
  <p class="t service" style="top:665px">Water<br>Extraction</p>
  <p class="t service" style="top:795px">Mold<br>Prevention</p>

  <p class="t ribbon-a">24/7</p>
  <p class="t ribbon-b">365 DAYS</p>

  <p class="t free">FREE</p>
  <p class="t evaluations">EVALUATIONS</p>

  <p class="t call-tab">CALL US TODAY</p>
  <p class="t phone">713-846-5170</p>
  <p class="t address">52710 Harlow Crossing Suite G4 Houston,<br>Texas 77193</p>
  <p class="t website">www.KESTRAL58129.example</p>
</main>
</body>
</html>
```